Corvale Real Estate

I manage 2 firms. The first one is Felmont and the logo is in blue (see the file) but i need a design for my business card for the second firm called CORVALE IMMOBILIER. This one is in charge of Real estate developer.

Colors
3176b5

```html
<!DOCTYPE html>
<html lang="en">
<head>
<meta charset="utf-8">
<title>Corvale Immobilier — Business Card</title>
<link href="https://fonts.googleapis.com/css2?family=Arimo:wght@400;700&display=swap" rel="stylesheet">
<style>
  :root {
    --page-bg: #2a2b2f;
    --card-bg: #1c2024;
    --brand-blue: #3176b5;
    --text-grey: #c9ccd1;
    --divider: #3176b5;
  }
  html, body {
    margin: 0;
    width: 1200px;
    height: 800px;
    overflow: hidden;
    background: var(--page-bg);
    font-family: "Arimo", Arial, sans-serif;
  }
  .stage {
    width: 1200px;
    height: 800px;
    display: flex;
    align-items: center;
    justify-content: center;
    gap: 60px;
  }
  .card {
    position: relative;
    width: 520px;
    height: 297px;
    background: var(--card-bg);
    border-radius: 16px;
    box-sizing: border-box;
  }
  .wordmark {
    color: var(--brand-blue);
    font-weight: 700;
    display: flex;
    align-items: center;
    gap: 12px;
  }
  .wordmark-square {
    width: 26px;
    height: 26px;
    background: var(--brand-blue);
    flex: none;
  }
  .wordmark-text {
    display: flex;
    flex-direction: column;
    line-height: 1;
  }
  .wordmark-name { font-size: 38px; letter-spacing: 6px; }
  .wordmark-sub { font-size: 13px; letter-spacing: 9px; margin-top: 8px; }

  .card-front {
    display: flex;
    align-items: center;
    justify-content: center;
  }

  .card-back {
    display: flex;
    align-items: center;
    padding: 0 30px 0 34px;
  }
  .card-back .wordmark-square { width: 18px; height: 18px; }
  .card-back .wordmark-name { font-size: 26px; letter-spacing: 4px; }
  .card-back .wordmark-sub { font-size: 9px; letter-spacing: 6px; margin-top: 6px; }
  .back-divider {
    width: 1px;
    height: 130px;
    background: var(--divider);
    margin: 0 22px 0 24px;
    flex: none;
  }
  .contact {
    color: var(--text-grey);
    font-size: 11.5px;
    line-height: 1.45;
  }
  .contact-name {
    color: var(--brand-blue);
    font-weight: 700;
    font-size: 15px;
    line-height: 1.1;
  }
  .contact-role { margin-bottom: 10px; }
  .contact-address { margin-bottom: 8px; }
  .contact-line {
    display: flex;
    align-items: center;
    gap: 7px;
  }
  .contact-icon { width: 11px; height: 11px; flex: none; }
</style>
</head>
<body>
<main class="stage">
  <section class="card card-front" aria-label="Card front">
    <div class="wordmark">
      <span class="wordmark-square"></span>
      <span class="wordmark-text">
        <span class="wordmark-name">CORVALE</span>
        <span class="wordmark-sub">IMMOBILIER</span>
      </span>
    </div>
  </section>

  <section class="card card-back" aria-label="Card back">
    <div class="wordmark">
      <span class="wordmark-square"></span>
      <span class="wordmark-text">
        <span class="wordmark-name">CORVALE</span>
        <span class="wordmark-sub">IMMOBILIER</span>
      </span>
    </div>
    <div class="back-divider"></div>
    <div class="contact">
      <div class="contact-name">MARC DELORME</div>
      <div class="contact-role">Manager</div>
      <div class="contact-address">PO BOX 48, Rue des Tilleuls<br>Quai Ouest, Lyon 69002</div>
      <div class="contact-line">
        <svg class="contact-icon" viewBox="0 0 12 12"><rect x="1.5" y="1.5" width="9" height="9" fill="none" stroke="#3176b5" stroke-width="1.6"/></svg>
        <span>(04) 781 2290</span>
      </div>
      <div class="contact-line">
        <svg class="contact-icon" viewBox="0 0 12 12"><rect x="0.5" y="2" width="11" height="8" fill="#3176b5"/><path d="M0.5 2 L6 6.5 L11.5 2" fill="none" stroke="#1c2024" stroke-width="1"/></svg>
        <span>info@corvale-immo.fr</span>
      </div>
      <div class="contact-line">
        <svg class="contact-icon" viewBox="0 0 12 12"><circle cx="6" cy="6" r="5.5" fill="#3176b5"/><path d="M0.5 6 H11.5 M6 0.5 C3 3.5 3 8.5 6 11.5 M6 0.5 C9 3.5 9 8.5 6 11.5" fill="none" stroke="#1c2024" stroke-width="0.8"/></svg>
        <span>www.corvale-immo.fr</span>
      </div>
    </div>
  </section>
</main>
</body>
</html>
```